Church Lanterns Over Millbrook Gospel Booklet Design

We need a booklet designed that we will be printing to hand out in our community. Wording for each page will be provided and we need graphic design to produce the layouts in a format ready for print. Booklet will be 4.75" x 4.75" square and a total of 12 pages: 1 cover page front, 1 cover page back, 10 inside pages some of which will be full spread across 2 pages.

Target Market(s)

English speaking Westerners

Industry/Entity Type

Religious

Font styles to use
Serif

Colors
ffffff
85abd2
0292cd
33b8a4
5c5c5c

Requirements
Must have
• Minimalist design with clean look described in attached document
Nice to have
• Aesthetically pleasing graphics, crisp fonts, excellent turn around times
Should not have
• Effeminate design, busy look with too much graphic and text

```html
<!DOCTYPE html>
<html lang="en">
<head>
<meta charset="utf-8">
<title>Lanterns Over Millbrook – Foundational Truths Spread</title>
<link href="https://fonts.googleapis.com/css2?family=Bodoni+Moda:ital,opsz,wght@0,6..96,400;1,6..96,400&display=swap" rel="stylesheet">
<style>
  :root {
    --white: #ffffff;
    --sky: #85abd2;
    --azure: #0292cd;
    --deep-blue: #1a8ad0;
    --ink: #1a1a1a;
    --grey: #5c5c5c;
  }
  * { margin: 0; padding: 0; box-sizing: border-box; }
  html, body { width: 1200px; height: 600px; overflow: hidden; background: var(--white); }
  .spread {
    position: relative;
    width: 1200px;
    height: 600px;
    overflow: hidden;
    font-family: "Bodoni Moda", "Times New Roman", serif;
    color: var(--ink);
  }
  .backdrop { position: absolute; inset: 0; }

  .truths-heading {
    position: absolute;
    left: 54px;
    top: 52px;
    width: 490px;
    height: 66px;
    background: var(--azure);
    color: var(--white);
    font-variant: small-caps;
    font-size: 24px;
    line-height: 30px;
    text-align: center;
    padding-top: 3px;
    letter-spacing: 0.5px;
  }
  .truths-list {
    position: absolute;
    left: 44px;
    top: 140px;
    width: 510px;
    list-style: none;
  }
  .truth {
    position: relative;
    padding-left: 26px;
    font-size: 24px;
    line-height: 29.5px;
    margin-bottom: 15px;
  }
  .truth-number { position: absolute; left: 0; top: 0; font-style: normal; }
  .truth-title { color: var(--azure); text-transform: uppercase; letter-spacing: -0.3px; }
  .truth-detail { font-style: italic; }

  .rebellion {
    position: absolute;
    left: 640px;
    top: 94px;
    width: 520px;
    text-align: center;
    font-style: italic;
    font-size: 24px;
    line-height: 29.5px;
  }
  .scripture {
    position: absolute;
    left: 640px;
    top: 318px;
    width: 520px;
    text-align: center;
    color: var(--azure);
    font-variant: small-caps;
    font-size: 27px;
    line-height: 34px;
    letter-spacing: 1px;
  }
  .citation {
    position: absolute;
    left: 640px;
    top: 494px;
    width: 520px;
    text-align: center;
    font-variant: small-caps;
    font-size: 18px;
  }
</style>
</head>
<body>
<main class="spread">
  <svg class="backdrop" width="1200" height="600" viewBox="0 0 1200 600" aria-hidden="true">
    <defs>
      <linearGradient id="sky-fade" x1="0" y1="0" x2="0" y2="1">
        <stop offset="0" stop-color="#1a8ad0"/>
        <stop offset="0.3" stop-color="#ffffff"/>
        <stop offset="0.7" stop-color="#ffffff"/>
        <stop offset="1" stop-color="#1a8ad0"/>
      </linearGradient>
    </defs>
    <rect width="1200" height="600" fill="url(#sky-fade)"/>
    <circle cx="300" cy="300" r="352" fill="#ffffff"/>
    <circle cx="900" cy="300" r="352" fill="#ffffff"/>
  </svg>

  <h2 class="truths-heading">This reality establishes some<br>foundational truths for all of us:</h2>

  <ol class="truths-list">
    <li class="truth"><span class="truth-number">1.</span><span class="truth-title">God loves us</span> <span class="truth-detail">- he didn’t have to create us; we are here because he couldn’t imagine life without us.</span></li>
    <li class="truth"><span class="truth-number">2.</span><span class="truth-title">God is the proper authority in our lives</span> <span class="truth-detail">- if he designed and made us, he rightfully owns us.</span></li>
    <li class="truth"><span class="truth-number">3.</span><span class="truth-title">God knows the purpose of our lives</span> <span class="truth-detail">- if he designed and made us, he knows why we are here.</span></li>
    <li class="truth"><span class="truth-number">4.</span><span class="truth-title">God’s truth is the truth we need</span> <span class="truth-detail">- if he designed and made us, he knows what it takes for life to go well for us.</span></li>
  </ol>

  <p class="rebellion">But we, mankind, have all rejected<br>God’s authority in our lives.<br>And because he rightfully owns us, our<br>rebellion against God is a grave injustice;<br>an act of treason for which we deserve to<br>be cut off<br>from God forever.</p>

  <blockquote class="scripture">“ For the wages of sin is death,<br>but the gift of God is eternal<br>life in[a] Christ Jesus our Lord”</blockquote>

  <p class="citation">(Romans 6:23)</p>
</main>
</body>
</html>
```